Create a wordpress website for Tavoro business solution

This project is to create a complete website with all pages.

Overview
The purpose of this project is to create a full complete website with all pages (16 pages). The site should be professional and modern. The site is for an IT recruiting and IT training company. The site needs to be easy to administer and update content. It should be simple to add pages, videos and testimonials later. I will leave the site layout, color schemes and flow to the designers.

Navigation Menu (Home, who we are, what we do, what makes us different, why it matters, candidate portal, contact us, Blog)

WHO WE ARE should be a drop down menu with link to pages (about us, mission, vision and purpose, our team)

WHAT WE DO should be drop down menu with link to the following pages (IT Recruiting, IT Training, Hardware and software sales)

What makes us different should be single page with different paragraph titles. (We live what we do, we don't compromise quality, we share knowledge, staffing guarantee)

Why it matters should be single page with paragraph titles. (Quickly fill positions, candidate career development)

Candidate portal should links to my portal login page. I can add the correct URL later. I just need it to link to somewhere. I can change it.

Contact us should have (address, phone number, google map and a form to submit request for a call back)

Blog - This link should launch a wordpress blogging module

Target Market(s)

IT RECRUITING AND CONSULTING

Industry/Entity Type

It Company

Coding

Coded - Design and coding required

Requirements
Must have
• Company Logo
• Navigation Menu (Home, who we are, what we do, what makes us different, why it matters, candidate portal, contact us)
• WHO WE ARE should be a drop down menu with link to pages (about us, mission, vision and purpose, our team)
• WHAT WE DO should be drop down menu with link to the following pages (IT Recruiting, IT Training, Hardware and software sales)
• What makes us different should be single page with different paragraph titles. (We live what we do, we don't compromise quality, we share knowledge, staffing guarantee)
• Why it matters should be single page with paragraph titles. (Quickly fill positions, candidate career development)
• Candidate portal should links to my portal login page. I can add the correct URL later. I just need it to link to somewhere. I can change it.
• Contact us should have (address, phone number, google map and a form to submit request for a call back)

```html
<!DOCTYPE html>
<html lang="en">
<head>
<meta charset="utf-8">
<title>Tavoro Business Solution</title>
<link href="https://fonts.googleapis.com/css2?family=Oswald:wght@300;400;500&family=PT+Sans:wght@400;700&family=PT+Sans+Narrow:wght@400;700&display=swap" rel="stylesheet">
<style>
:root{
  --blue:#0b56a2;
  --blue-dark:#08457f;
  --orange:#e8772a;
  --ink:#1c1c1c;
  --text:#444;
  --muted:#8a8a8a;
  --line:#d6d6d6;
  --dark:#1d2126;
  --white:#fff;
}
*{box-sizing:border-box;margin:0;padding:0}
html,body{width:1200px;height:3681px;overflow:hidden}
body{font-family:"PT Sans",Arial,sans-serif;color:var(--text);background:var(--white);position:relative}
.section{position:absolute;left:0;width:1200px}
a{color:inherit;text-decoration:none}

/* hero */
.hero{top:0;height:798px}
.hero-photo{position:absolute;inset:0;background:linear-gradient(100deg,#2a2d33 0%,#4a4d55 30%,#6b6a70 55%,#2b3550 80%,#1a2238 100%)}
.hero-shade{position:absolute;inset:0;background:linear-gradient(90deg,rgba(0,0,0,.45),rgba(0,0,0,.1) 60%,rgba(0,0,0,.2))}
.topbar{position:absolute;top:0;left:0;width:1200px;height:60px;color:#fff;font-size:19px}
.topbar .phone{position:absolute;left:520px;top:17px;display:flex;gap:10px;align-items:center}
.topbar .mail{position:absolute;left:744px;top:17px;display:flex;gap:10px;align-items:center}
.topbar .search{position:absolute;left:943px;top:16px;width:200px;height:22px;border-bottom:1px solid #fff}
.topbar .search svg{position:absolute;right:0;top:0}
.nav{position:absolute;top:60px;left:0;width:1200px;height:92px;background:var(--blue)}
.brand{position:absolute;left:0;top:0;width:318px;height:92px;background:#fff;clip-path:polygon(0 0,100% 0,88% 100%,0 100%);display:flex;align-items:center;padding-left:44px;gap:12px}
.brand .mark{width:18px;height:18px;background:var(--orange)}
.brand .name{font-family:"PT Sans",sans-serif;font-weight:700;font-size:30px;color:var(--blue)}
.menu{position:absolute;left:318px;top:38px;display:flex;gap:22px;font-family:"PT Sans Narrow",sans-serif;font-size:18px;color:#fff}
.menu .active{border-bottom:2px solid #fff;padding-bottom:6px}
.hero-copy{position:absolute;left:44px;top:302px;color:#fff}
.hero-copy .kicker{font-family:"Oswald",sans-serif;font-weight:300;font-size:34px}
.hero-copy h1{font-family:"Oswald",sans-serif;font-weight:400;font-size:80px;line-height:1;margin-top:14px;letter-spacing:.5px}
.hero-copy p{font-size:18px;line-height:1.6;width:720px;margin-top:18px}
.btn-quote{position:absolute;left:44px;top:560px;width:246px;height:48px;background:#fff;display:flex;align-items:center;font-family:"PT Sans",sans-serif;font-weight:700;font-size:17px;color:var(--ink);padding-left:14px}
.btn-quote .arr{position:absolute;right:0;top:0;width:48px;height:48px;background:var(--blue);display:flex;align-items:center;justify-content:center}

/* about */
.tabs-main{top:836px;left:0;width:1200px;display:flex;justify-content:center;gap:58px;font-family:"PT Sans",sans-serif;font-size:23px;color:var(--ink)}
.tabs-main .on{border-bottom:2px solid var(--blue);padding:0 14px 6px}
.tabs-main .on::before{content:"";position:absolute}
.about-frame{position:absolute;left:44px;top:908px;width:392px;height:424px;border:10px solid var(--blue)}
.about-frame-line{position:absolute;left:90px;top:940px;width:396px;height:448px;border:2px solid var(--orange)}
.about-photo{position:absolute;left:90px;top:942px;width:400px;height:428px;background:linear-gradient(135deg,#d9dde0,#8f9aa3 45%,#2b2f38 70%,#c9ccd0)}
.about-copy{position:absolute;left:536px;top:972px;width:610px}
.about-copy h2{font-family:"PT Sans",sans-serif;font-weight:700;font-size:26px;color:var(--ink);margin-bottom:22px}
.about-copy p{font-size:15px;line-height:1.65;text-align:justify;margin-bottom:16px}
.btn-more{display:inline-flex;align-items:center;width:150px;height:38px;border:2px solid var(--ink);position:relative}
.btn-more .lbl{background:var(--ink);color:#fff;font-size:12px;height:100%;width:110px;display:flex;align-items:center;justify-content:center}
.btn-more .arr{flex:1;display:flex;align-items:center;justify-content:center}

/* what we do */
.wwd{top:1438px;height:518px}
.wwd-photo{position:absolute;left:0;top:0;width:592px;height:518px;background:linear-gradient(160deg,#e8e4df,#b8aa9c 40%,#6c5e55 70%,#3a3430)}
.wwd-panel{position:absolute;left:592px;top:0;width:608px;height:518px;background:var(--blue);color:#fff;padding:48px 48px}
.wwd-panel h2{font-family:"PT Sans",sans-serif;font-weight:700;font-size:26px;margin-bottom:24px}
.service{display:flex;gap:22px;margin-bottom:22px}
.service .ico{width:56px;height:56px;background:#fff;flex:none;display:flex;align-items:center;justify-content:center;margin-top:6px}
.service h3{font-weight:700;font-size:21px;margin-bottom:2px}
.service p{font-size:15px;line-height:1.3}

/* different */
.title{font-family:"PT Sans",sans-serif;font-weight:700;font-size:26px;color:var(--ink);text-align:center}
.title::after{content:"";display:block;width:120px;height:2px;background:var(--ink);margin:10px auto 0}
.diff-title{top:1998px}
.diff-tabs{top:2074px;left:44px;display:flex;gap:12px}
.diff-tabs span{height:34px;padding:0 22px;display:flex;align-items:center;font-size:15px;background:var(--blue);color:#fff}
.diff-tabs span.on{background:#fff;color:var(--ink);border:1px solid var(--blue);border-bottom:none;height:35px}
.diff-box{top:2108px;left:44px;width:1092px;height:137px;border:1px solid var(--blue);padding:18px 16px;font-size:13px;line-height:1.75;color:var(--text)}

/* why it matters */
.why-title{top:2284px}
.slider{top:2353px;left:44px;width:1095px;height:403px}
.slide-photo{position:absolute;left:440px;top:0;width:655px;height:403px;background:linear-gradient(120deg,#e9eef3,#b9c6d3 40%,#4b5a6c 65%,#dfe5ea)}
.slide-panel{position:absolute;left:0;top:0;width:620px;height:403px;background:var(--blue);clip-path:polygon(0 0,78% 0,100% 100%,0 100%);color:#fff;padding:46px 64px}
.slide-panel h2{font-family:"PT Sans",sans-serif;font-weight:700;font-size:38px;line-height:1.2}
.slide-panel p{font-size:18px;line-height:1.4;margin-top:26px;width:440px}
.slide-panel .url{font-size:18px;margin-top:24px}
.slide-panel .btn-more{margin-top:18px;border-color:#fff}
.slide-arrow{position:absolute;top:178px;width:34px;height:34px;background:#111;display:flex;align-items:center;justify-content:center}

/* jobs */
.jobs{top:2800px;height:385px;background:linear-gradient(90deg,#15181c,#2a2f35 60%,#1a1d21);color:#fff}
.jobs h2{position:absolute;left:44px;top:42px;font-weight:400;font-size:32px}
.jobs .sub{position:absolute;left:44px;top:86px;font-size:21px}
.field{position:absolute;top:152px;height:50px;background:#fff;color:var(--muted);display:flex;align-items:center;gap:14px;padding-left:14px;font-size:17px}
.btn-search{position:absolute;left:972px;top:152px;width:166px;height:50px;background:var(--blue);color:#fff;font-size:20px;display:flex;align-items:center;justify-content:center}
.tags{position:absolute;left:44px;top:236px;display:grid;grid-template-columns:repeat(4,250px);column-gap:28px;row-gap:22px}
.tag{display:flex;justify-content:space-between;align-items:center;height:34px;border-bottom:1px solid #8a8f96;font-size:17px}
.tag b{width:22px;height:22px;border:1px solid #aaa;border-radius:50%;font-size:11px;font-weight:400;display:flex;align-items:center;justify-content:center}

/* call back */
.callback{top:3216px;left:44px;width:620px}
.callback .eyebrow{font-size:26px;color:var(--ink)}
.callback h2{font-family:"PT Sans",sans-serif;font-weight:700;font-size:34px;color:var(--ink);margin-top:6px}
.callback .q{font-size:18px;color:var(--ink);margin-top:4px}
.form{display:grid;grid-template-columns:308px 308px;gap:6px 2px;margin-top:20px}
.form span{height:50px;border:1px solid var(--line);display:flex;align-items:center;padding-left:20px;font-size:16px;color:var(--muted)}
.form span.focus{border:2px solid var(--ink);color:var(--ink)}
.btn-submit{margin-top:24px;width:138px;height:50px;background:var(--blue);color:#fff;font-size:21px;display:flex;align-items:center;justify-content:center}
.map{top:3244px;left:682px;width:457px;height:312px;border:2px solid var(--blue);background:linear-gradient(135deg,#eef0ec,#dfe5dc 50%,#e9ece6)}

/* footer */
.footer{top:3602px;height:79px;background:var(--blue);color:#fff;text-align:center;font-size:13px}
.footer .links{padding-top:20px;word-spacing:2px}
.footer .links i{font-style:normal;margin:0 12px}
.footer .copy{margin-top:8px}
</style>
</head>
<body>

<header class="section hero">
  <div class="hero-photo" role="img" aria-label="Photo of a speaker presenting to an audience at a business event"></div>
  <div class="hero-shade"></div>
  <div class="topbar">
    <div class="phone"><svg width="20" height="20" viewBox="0 0 24 24"><path fill="#fff" d="M6.6 10.8a15 15 0 006.6 6.6l2.2-2.2a1 1 0 011-.25 11.4 11.4 0 003.6.6 1 1 0 011 1V20a1 1 0 01-1 1A17 17 0 013 4a1 1 0 011-1h3.5a1 1 0 011 1c0 1.25.2 2.45.6 3.6a1 1 0 01-.25 1z"/></svg>(+000) 123 45 678</div>
    <div class="mail"><svg width="22" height="16" viewBox="0 0 22 16"><rect x="1" y="1" width="20" height="14" fill="none" stroke="#fff" stroke-width="1.6"/><path d="M1 1l10 8 10-8" fill="none" stroke="#fff" stroke-width="1.6"/></svg>info@tavoro.com</div>
    <div class="search"><svg width="20" height="20" viewBox="0 0 20 20"><circle cx="12" cy="8" r="6" fill="none" stroke="#fff" stroke-width="2"/><path d="M8 12l-6 6" stroke="#fff" stroke-width="2.4"/></svg></div>
  </div>
  <nav class="nav">
    <div class="brand"><span class="mark"></span><span class="name">tavoro</span></div>
    <div class="menu">
      <span class="active">HOME</span><span>WHO WE ARE</span><span>WHAT WE DO</span><span>WHAT MAKES US DIFFERENT</span><span>WHY IT MATTERS</span><span>CANDIDATE PORTAL</span><span>CONTACT</span>
    </div>
  </nav>
  <div class="hero-copy">
    <div class="kicker">WE ARE EXPERT</div>
    <h1>EXPERIENCE GREAT SERVICE</h1>
    <p>Duis autem vel eum iriure dolor in hendrerit in vulputate velit &nbsp;esse molestie dolore eu feugiat nulla facilisis at vero eros et accumsan et iusto.</p>
  </div>
  <a class="btn-quote">REQUEST A QUOTE<span class="arr"><svg width="12" height="18" viewBox="0 0 12 18"><path d="M2 2l7 7-7 7" fill="none" stroke="#fff" stroke-width="2.5"/></svg></span></a>
</header>

<div class="section tabs-main"><span class="on">ABOUT</span><span>MISSION</span><span>VISION</span><span>PURPOSE</span><span>OUR TEAM</span></div>

<section class="about">
  <div class="about-frame"></div>
  <div class="about-photo" role="img" aria-label="Photo of a smiling businessman in a suit shaking hands"></div>
  <div class="about-frame-line"></div>
  <div class="about-copy">
    <h2>WELCOME TO TAVORO</h2>
    <p>Lorem ipsum dolor sit amet, consectetur adipiscing elit. Nullam vitae maximus mauris. Ut sollicitudin scelerisque finibus. Suspendisse scelerisque porta ante, vel blandit metus lacinia sit amet. Ut quis lacus non lorem volutpat gravida. Nulla condimentum massa nunc, ac congue lectus sollicitudin id. Nulla bibendum egestas felis, quis rhoncus leo facilisis ut. Vivamus euismod commodo imperdiet.</p>
    <p>Nulla in nibh a dui porta ultricies. Aliquam varius metus eu est auctor, sit amet efficitur nisl iaculis. Fusce vitae velit maximus, bibendum nisl quis, blandit nibh. Pellentesque odio nisi, egestas id sollicitudin non, suscipit non urna. Suspendisse vel ex felis. Nulla sollicitudin mollis est. Aliquam euismod mattis</p>
    <a class="btn-more"><span class="lbl">READ MORE</span><span class="arr"><svg width="10" height="14" viewBox="0 0 10 14"><path d="M2 2l5 5-5 5" fill="none" stroke="#1c1c1c" stroke-width="2"/></svg></span></a>
  </div>
</section>

<section class="section wwd">
  <div class="wwd-photo" role="img" aria-label="Photo of an audience seated at a conference"></div>
  <div class="wwd-panel">
    <h2>WHAT WE DO</h2>
    <div class="service"><span class="ico"><svg width="34" height="34" viewBox="0 0 34 34"><circle cx="17" cy="17" r="13" fill="none" stroke="#0b56a2" stroke-width="3"/><circle cx="17" cy="17" r="6" fill="none" stroke="#0b56a2" stroke-width="3"/><circle cx="17" cy="17" r="2" fill="#0b56a2"/></svg></span><div><h3>IT RECRUITING</h3><p>Duis fermentum et augue in faucibus. Nam lobortis ultricies<br>nunc a tristique enim congue nec uisque ac nisi semuis</p></div></div>
    <div class="service"><span class="ico"><svg width="34" height="34" viewBox="0 0 34 34"><rect x="12" y="5" width="19" height="14" fill="none" stroke="#0b56a2" stroke-width="2.5"/><circle cx="7" cy="12" r="3.5" fill="#0b56a2"/><rect x="3" y="17" width="8" height="13" fill="#0b56a2"/><path d="M10 19l8-4" stroke="#0b56a2" stroke-width="2.5"/></svg></span><div><h3>IT TRAINING</h3><p>Duis fermentum et augue in faucibus. Nam lobortis ultricies<br>nunc a tristique enim congue nec uisque ac nisi semuis</p></div></div>
    <div class="service"><span class="ico"><svg width="34" height="34" viewBox="0 0 34 34"><path d="M6 6l22 22M28 6L6 28" stroke="#0b56a2" stroke-width="5" stroke-linecap="round"/></svg></span><div><h3>HARDWARE</h3><p>Duis fermentum et augue in faucibus. Nam lobortis ultricies<br>nunc a tristique enim congue nec uisque ac nisi semuis</p></div></div>
    <div class="service"><span class="ico"><svg width="36" height="34" viewBox="0 0 36 34"><rect x="3" y="4" width="30" height="20" fill="none" stroke="#0b56a2" stroke-width="3"/><path d="M12 30h12M18 24v6" stroke="#0b56a2" stroke-width="3"/></svg></span><div><h3>SOFTWARE SALES</h3><p>Duis fermentum et augue in faucibus. Nam lobortis ultricies<br>nunc a tristique enim congue nec uisque ac nisi semuis</p></div></div>
  </div>
</section>

<h2 class="section title diff-title">WHAT MAKES US DIFFERENT</h2>
<div class="section diff-tabs"><span class="on">We live what we do</span><span>We don't compromise quality</span><span>We share knowledge</span><span>Staffing Guarantee</span></div>
<div class="section diff-box">Lorem ipsum dolor sit amet, consectetur adipiscing elit. Nunc eget dui nisl. Mauris sed dolor scelerisque, pellentesque ipsum nec, vehicula quam. Donec cursus arcu dolor, ut interdum massa elementum sed. Ut eget lorem tellus. Vivamus suscipit massa ut aliquet pretium. Suspendisse id ante quis magna accumsan dictum. Quisque eleifend massa in risus facilisis sagittis. Sed congue dui quis ipsum pellentesque porta. Nullam est justo, molestie eget diam vitae, pharetra semper mauris. In pellentesque placerat elit ac interdum. Etiam lorem dui, rhoncus a luctus eget, sollicitudin hendrerit nibh. Duis ultrices interdum nulla et commodo.</div>

<h2 class="section title why-title">WHY IT MATTERS</h2>
<section class="section slider">
  <div class="slide-photo" role="img" aria-label="Photo of three colleagues meeting at an office table with a laptop"></div>
  <div class="slide-panel">
    <h2>QUICKLY FILL<br>POSITIONS</h2>
    <p>Lorem ipsum dolor sit amet, consectetur adipiscing Quisque sodales mollis elit quis ornare. Suspendisse facilisis leo ac leo imperdiet iaculis.</p>
    <div class="url">www.tavoro.com</div>
    <a class="btn-more"><span class="lbl">READ MORE</span><span class="arr"><svg width="10" height="14" viewBox="0 0 10 14"><path d="M2 2l5 5-5 5" fill="none" stroke="#fff" stroke-width="2"/></svg></span></a>
  </div>
  <span class="slide-arrow" style="left:0"><svg width="10" height="14" viewBox="0 0 10 14"><path d="M8 2L3 7l5 5" fill="none" stroke="#fff" stroke-width="2.4"/></svg></span>
  <span class="slide-arrow" style="right:0"><svg width="10" height="14" viewBox="0 0 10 14"><path d="M2 2l5 5-5 5" fill="none" stroke="#fff" stroke-width="2.4"/></svg></span>
</section>

<section class="section jobs" role="region" aria-label="Job search">
  <h2>Search from 22 job offers</h2>
  <div class="sub">Your career starts here.</div>
  <div class="field" style="left:44px;width:370px"><svg width="20" height="20" viewBox="0 0 20 20"><circle cx="8" cy="8" r="6" fill="none" stroke="#333" stroke-width="2"/><path d="M12.5 12.5l6 6" stroke="#333" stroke-width="2.4"/></svg>Keywords</div>
  <div class="field" style="left:508px;width:438px"><svg width="18" height="22" viewBox="0 0 18 22"><path d="M9 21s7-7 7-12A7 7 0 002 9c0 5 7 12 7 12z" fill="none" stroke="#555" stroke-width="1.6"/><circle cx="9" cy="9" r="2.6" fill="none" stroke="#555" stroke-width="1.6"/></svg>Location</div>
  <a class="btn-search">SEARCH</a>
  <div class="tags">
    <div class="tag">Webdesinger<b>8</b></div><div class="tag">Business Excutive<b>4</b></div><div class="tag">Developer<b>2</b></div><div class="tag">Freelancer<b>5</b></div>
    <div class="tag">PHP Developer<b>4</b></div><div class="tag">UI Developer<b>3</b></div><div class="tag">Software Developer<b>7</b></div><div class="tag">Marketing<b>5</b></div>
  </div>
</section>

<section class="section callback">
  <div class="eyebrow">call back</div>
  <h2>REQUEST A CALL BACK</h2>
  <div class="q">How can we help?</div>
  <div class="form">
    <span class="focus">Address</span><span>Name</span>
    <span>Email</span><span>Phone Number</span>
  </div>
  <a class="btn-submit">SUBMIT</a>
</section>
<div class="section map" role="img" aria-label="Street map showing the office location"></div>

<footer class="section footer">
  <div class="links">Home<i>/</i>Who We Are<i>/</i>What We do<i>/</i>What Makes us Different<i>/</i>Why it matters<i>/</i>Candidate Portal<i>/</i>Contact</div>
  <div class="copy">© 2016 Tavoro All Rights Reserved.</div>
</footer>

</body>
</html>
```